Email Signature

We are looking for creative email signature for our company. Please find attached the logo of our company for your reference. now we understand there isn't much can be done with email signature but we are looking for out of the box designs. Nothing specific in mind

Please insert fake numbers, website and/or address, etc just to showcase the designs. once the design is chosen we will provide the actual details.

Dear All,

We wouldlike to extend our apology for not being able to provide feedbacks to everysingle design. We were extremely busy and we have multiple contests opensimultaneously which makes the process harder. However, thank you all for theefforts you have put into this contest. We have received anoverwhelming quality responses & it has been a very difficult task tochoose just one, we easily Loved at least several designs...

Thanksagain for participating, we wish you all success in your design ventures.

Kindregards,

HLG Team

Industry/Entity Type

It Company

```html
<!DOCTYPE html>
<html lang="en">
<head>
<meta charset="utf-8">
<title>Harbor Lantern Group – Email Signature &amp; Letterhead</title>
<link rel="stylesheet" href="https://fonts.googleapis.com/css2?family=Arimo:wght@400;700&family=Barlow:wght@500&family=PT+Sans:wght@400&display=swap">
<style>
  :root{
    --canvas-top:#e9ecee;
    --canvas-bottom:#d8dcdf;
    --brand-green:#8cc63f;
    --brand-blue:#2f86c8;
    --panel-grey:#e8e9ea;
    --ink:#111111;
    --ink-soft:#333333;
    --photo-light:#7d9cbc;
    --photo-dark:#274a74;
    --bar-top:#ffffff;
    --bar-bottom:#a6a8ab;
    --icon-light:#f2f2f2;
    --icon-dark:#b4b6b9;
    --paper:#ffffff;
  }
  *{box-sizing:border-box;margin:0;padding:0}
  html,body{width:1200px;height:910px;overflow:hidden}
  body{
    position:relative;
    background:linear-gradient(180deg,var(--canvas-top),var(--canvas-bottom));
    font-family:"Arimo",Arial,sans-serif;
    color:var(--ink);
  }

  .sign-off{
    position:absolute;
    font-family:"Barlow",Arial,sans-serif;font-weight:500;
    color:var(--brand-blue);
  }

  /* ---------- signature block ---------- */
  .signature{
    position:absolute;width:585px;height:170px;
    background:var(--panel-grey);
    transform-origin:top left;
  }
  .signature__art{position:absolute;left:0;top:0}
  .signature__name{
    position:absolute;left:47px;top:2px;
    font-size:15px;line-height:16px;color:var(--ink);
  }
  .signature__name strong{display:block;font-weight:700}
  .signature__address{
    position:absolute;left:47px;top:50px;
    font-size:11px;line-height:13px;
  }
  .signature__contacts{
    position:absolute;left:47px;top:78px;
    font-size:11px;line-height:13px;
  }
  .signature__contacts div{display:flex}
  .signature__contacts b{width:48px;font-weight:700}
  .signature__contacts a{color:inherit;text-decoration:none}
  .signature__brand{
    position:absolute;left:330px;top:44px;width:250px;text-align:center;
    font-size:28px;font-weight:700;color:#ffffff;letter-spacing:-0.5px;
  }
  .signature__bar{
    position:absolute;left:0;top:125px;width:585px;height:45px;
    background:linear-gradient(180deg,var(--bar-top) 0%,#ececed 45%,var(--bar-bottom) 100%);
  }
  .signature__contact-label{
    position:absolute;left:46px;top:15px;font-size:12px;
  }
  .signature__social{position:absolute;left:121px;top:8px;overflow:visible}
  .signature__web{
    position:absolute;right:10px;top:14px;
    font-size:13px;font-weight:700;color:var(--ink-soft);
  }

  .disclaimer{
    position:absolute;
    font-family:"PT Sans",Arial,sans-serif;
    font-size:5.4px;line-height:6.6px;color:var(--ink-soft);
  }

  /* ---------- letterhead page ---------- */
  .letter{
    position:absolute;left:647px;top:213px;width:399px;height:542px;
    background:var(--paper);border-radius:9px;
    box-shadow:0 2px 6px rgba(0,0,0,.18);
    overflow:hidden;
  }
  .letter__salutation{
    position:absolute;left:29px;top:128px;
    font-family:"PT Sans",Arial,sans-serif;font-size:10px;color:var(--ink);
  }
  .letter__body{
    position:absolute;left:29px;top:163px;width:324px;
    font-family:"PT Sans",Arial,sans-serif;font-size:7.3px;line-height:10.6px;
    text-align:justify;color:var(--ink);
  }
  .letter__body p+p{margin-top:13px}
</style>
</head>
<body>

<!-- Email signature -->
<p class="sign-off" style="left:71px;top:303px;font-size:13px">Kind Regards,</p>

<div class="signature" style="left:25px;top:338px">
  <svg class="signature__art" width="585" height="125" viewBox="0 0 585 125">
    <defs>
      <linearGradient id="photoTone" x1="0" y1="0" x2="0" y2="1">
        <stop offset="0" stop-color="var(--photo-light)"/>
        <stop offset="1" stop-color="var(--photo-dark)"/>
      </linearGradient>
    </defs>
    <polygon points="22,0 330,0 305,39 8,39" fill="var(--brand-green)"/>
    <polygon points="334,0 340,0 276,125 270,125" fill="#ffffff"/>
    <polygon points="342,2 585,2 585,125 278,125" fill="url(#photoTone)" role="img" aria-label="City skyline photograph"/>
  </svg>
  <div class="signature__name">Ben Calloway<strong>Director</strong></div>
  <div class="signature__address">82 Tidewater Lane<br>Portside, Australia 2730</div>
  <div class="signature__contacts">
    <div><b>Phone:</b>+ 64 5550 1937</div>
    <div><b>Mobile:</b>0400 555 318</div>
    <div><b>Email:</b><span>ben.a@harborlantern.com</span></div>
  </div>
  <div class="signature__brand">HarborLantern</div>
  <div class="signature__bar">
    <span class="signature__contact-label">Contact Us</span>
    <svg class="signature__social" width="140" height="30" viewBox="0 0 140 30">
      <defs>
        <radialGradient id="iconTone" cx="0.4" cy="0.35" r="0.7">
          <stop offset="0" stop-color="var(--icon-light)"/>
          <stop offset="1" stop-color="var(--icon-dark)"/>
        </radialGradient>
      </defs>
      <path d="M-6 6 Q2 -4 12 0" fill="none" stroke="var(--brand-blue)" stroke-width="2.5"/>
      <polygon points="11,-4 16,2 8,3" fill="var(--brand-blue)"/>
      <circle cx="14" cy="14" r="12" fill="url(#iconTone)" stroke="#c9cbcd"/>
      <circle cx="50" cy="14" r="12" fill="url(#iconTone)" stroke="#c9cbcd"/>
      <circle cx="85" cy="14" r="12" fill="url(#iconTone)" stroke="#c9cbcd"/>
      <circle cx="120" cy="14" r="12" fill="url(#iconTone)" stroke="#c9cbcd"/>
    </svg>
    <span class="signature__web">www.harborlantern.com</span>
  </div>
</div>

<p class="disclaimer" style="left:37px;top:519px;width:548px">This email and any files sent with it are private and meant only for the person or group to whom they are addressed. If you received this email by mistake please tell the sender at once and delete it from your system. Any copying, sharing or use of its contents by anyone other than the intended recipient is not allowed. Please consider the environment before you print this message and keep all details safe.</p>

<!-- Letterhead -->
<div class="letter">
  <p class="letter__salutation">Dear Mr. Hale,</p>
  <div class="letter__body">
    <p>Lorem ipsum dolor sit amet, consectetur adipiscing elit. Donec orci purus, luctus vitae dignissim eu, iaculis sed purus. Vivamus faucibus, ipsum nec aliquet viverra, leo mauris condimentum ligula, sit amet sagittis enim ligula quis arcu. Nam egestas tortor id nisi porttitor mattis. In tortor ante, ultricies in suscipit a, tempus non massa. Vivamus et auctor mi. Fusce vel massa nulla. Phasellus nec eros mauris, et scelerisque orci. Donec malesuada orci vitae nulla accumsan porta a id massa. Quisque accumsan iaculis magna sit amet fringilla. Maecenas consequat, magna eget tincidunt semper, odio nibh rutrum mi, id feugiat ante nisi eu risus. Vestibulum nunc orci, rhoncus a placerat in, ultricies in mi. Cras mattis varius eros, vel fringilla nisi suscipit eget.</p>
    <p>Quisque scelerisque sagittis nulla at porttitor. Mauris a justo et tellus interdum tristique. Sed id augue vitae urna euismod commodo aliquet a quam. Pellentesque arcu velit, cursus et malesuada ut, consequat et diam. Nullam erat sem, rhoncus id ullamcorper vitae, rhoncus et arcu. In ultricies ultricies nulla, ut rutrum nisi iaculis at. Donec eu magna a metus ornare faucibus. Fusce aliquet faucibus ultricies. Morbi semper, est id tincidunt gravida, sem arcu adipiscing lacus, ac bibendum nulla leo eu purus. Quisque nec diam sed risus consectetur a accumsan quis quis nibh. Vestibulum id purus lorem.</p>
  </div>
  <p class="sign-off" style="left:30px;top:371px;font-size:9px">Kind Regards,</p>
  <div class="signature" style="left:0;top:396px;transform:scale(0.682)">
    <svg class="signature__art" width="585" height="125" viewBox="0 0 585 125">
      <defs>
        <linearGradient id="photoToneLetter" x1="0" y1="0" x2="0" y2="1">
          <stop offset="0" stop-color="var(--photo-light)"/>
          <stop offset="1" stop-color="var(--photo-dark)"/>
        </linearGradient>
      </defs>
      <polygon points="22,0 330,0 305,39 8,39" fill="var(--brand-green)"/>
      <polygon points="334,0 340,0 276,125 270,125" fill="#ffffff"/>
      <polygon points="342,2 585,2 585,125 278,125" fill="url(#photoToneLetter)" role="img" aria-label="City skyline photograph"/>
    </svg>
    <div class="signature__name">Ben Calloway<strong>Director</strong></div>
    <div class="signature__address">82 Tidewater Lane<br>Portside, Australia 2730</div>
    <div class="signature__contacts">
      <div><b>Phone:</b>+ 64 5550 1937</div>
      <div><b>Mobile:</b>0400 555 318</div>
      <div><b>Email:</b><span>ben.a@harborlantern.com</span></div>
    </div>
    <div class="signature__brand">HarborLantern</div>
    <div class="signature__bar">
      <span class="signature__contact-label">Contact Us</span>
      <svg class="signature__social" width="140" height="30" viewBox="0 0 140 30">
        <path d="M-6 6 Q2 -4 12 0" fill="none" stroke="var(--brand-blue)" stroke-width="2.5"/>
        <polygon points="11,-4 16,2 8,3" fill="var(--brand-blue)"/>
        <circle cx="14" cy="14" r="12" fill="url(#iconTone)" stroke="#c9cbcd"/>
        <circle cx="50" cy="14" r="12" fill="url(#iconTone)" stroke="#c9cbcd"/>
        <circle cx="85" cy="14" r="12" fill="url(#iconTone)" stroke="#c9cbcd"/>
        <circle cx="120" cy="14" r="12" fill="url(#iconTone)" stroke="#c9cbcd"/>
      </svg>
      <span class="signature__web">www.harborlantern.com</span>
    </div>
  </div>
  <p class="disclaimer" style="left:7px;top:518px;width:385px;font-size:3.8px;line-height:4.6px">This email and any files sent with it are private and meant only for the person or group to whom they are addressed. If you received this email by mistake please tell the sender at once and delete it from your system. Any copying, sharing or use of its contents by anyone other than the intended recipient is not allowed. Please consider the environment before you print this message and keep all details safe.</p>
</div>

</body>
</html>
```